Lena Corvell Business Card

I need a business card that reflects my current website: itslenacorvell.example and screenshot attached. If we keep the color scheme of the site and sample card below that would be ideal. The business card should include the information on the attached sample cards.

Industry/Entity Type

Business

```html
<!DOCTYPE html>
<html lang="en">
<head>
<meta charset="utf-8">
<title>Lena Corvell Business Card</title>
<link rel="stylesheet" href="https://fonts.googleapis.com/css2?family=Open+Sans:wght@400;500&display=swap">
<style>
  :root {
    --page: #e9e7e4;
    --card: #ffffff;
    --ink: #3b4049;
    --teal: #4cae98;
    --teal-band: #5cc2ad;
    --slate: #2c323a;
    --denim: #7d93ad;
    --skin: #a8673f;
    --hair: #8a4a22;
  }
  html, body {
    margin: 0;
    width: 1200px;
    height: 900px;
    overflow: hidden;
    background: var(--page);
  }
  .canvas {
    position: relative;
    width: 1200px;
    height: 900px;
  }
  .card {
    position: absolute;
    left: 75px;
    top: 150px;
    width: 1050px;
    height: 600px;
    background: var(--card);
    overflow: hidden;
    box-shadow: 0 4px 14px rgba(0,0,0,0.18);
    font-family: "Open Sans", Arial, sans-serif;
  }
  .card__bands {
    position: absolute;
    left: 0;
    top: 0;
    width: 1050px;
    height: 600px;
  }
  .identity {
    position: absolute;
    left: 40px;
    top: 70px;
    width: 600px;
    text-align: center;
    color: var(--ink);
  }
  .identity__name {
    margin: 0;
    font-size: 54px;
    font-weight: 400;
    letter-spacing: 1px;
    line-height: 1;
    text-transform: uppercase;
  }
  .identity__roles {
    margin: 14px 0 0;
    font-size: 23px;
    font-weight: 500;
    line-height: 1.2;
  }
  .contact {
    position: absolute;
    left: 40px;
    top: 190px;
    width: 600px;
    text-align: center;
    color: var(--teal);
    font-size: 26px;
    line-height: 38px;
  }
  .contact p { margin: 0; }
  .contact__group + .contact__group { margin-top: 38px; }
  .portrait {
    position: absolute;
    left: 650px;
    top: 20px;
    width: 400px;
    height: 580px;
    border-radius: 180px 180px 0 0;
    background: linear-gradient(180deg, var(--hair) 0%, var(--skin) 35%, var(--skin) 55%, var(--denim) 72%, var(--denim) 100%);
  }
  .signature {
    position: absolute;
    left: 190px;
    top: 480px;
    width: 380px;
    height: 80px;
    border-radius: 6px;
    background: var(--denim);
    opacity: 0.55;
  }
</style>
</head>
<body>
<div class="canvas">
  <div class="card">
    <svg class="card__bands" viewBox="0 0 1050 600" aria-hidden="true">
      <path fill="var(--teal-band)" d="M0 470 L30 462 L55 470 L80 455 L110 462 L140 448 L170 455 L200 440 L230 447 L260 432 L290 440 L320 424 L350 432 L380 418 L410 425 L440 408 L470 416 L500 400 L530 410 L560 395 L590 402 L620 388 L650 396 L680 384 L710 390 L740 380 L770 386 L800 376 L1050 376 L1050 600 L0 600 Z"/>
      <path fill="var(--slate)" d="M0 500 L25 492 L50 500 L80 486 L110 494 L140 478 L170 486 L200 470 L230 478 L260 462 L290 470 L320 455 L350 462 L380 446 L410 455 L440 438 L470 446 L500 430 L530 440 L560 424 L590 432 L620 418 L650 426 L680 412 L710 420 L740 406 L770 414 L800 402 L1050 402 L1050 600 L0 600 Z"/>
    </svg>

    <header class="identity">
      <h1 class="identity__name">Lena Corvell</h1>
      <p class="identity__roles">Brand Curator | Digital Storyteller | Social Entrpreneur</p>
    </header>

    <address class="contact">
      <div class="contact__group">
        <p>me@lenacorvell.example</p>
        <p>555.013.4270</p>
      </div>
      <div class="contact__group">
        <p>[fb] | [t.] | [ig] @itslenacorvell</p>
        <p>www.itslenacorvell.example</p>
      </div>
    </address>

    <div class="portrait" role="img" aria-label="Illustrated portrait of a smiling woman with short curly hair in a denim shirt"></div>
    <div class="signature" role="img" aria-label="Hand-lettered signature reading 'its Lena Corvell'"></div>
  </div>
</div>
</body>
</html>
```